Brochure Design - Marketing Document - real estate development

It is a 7 Page Proposal document. Please see attached example. It will be used as a marketing proposal document given to potential clients. It is a 'capability statement' used to demonstrate the capability and expertise of the business. I will provide all images and copy to be used in the document. I just need someone to create the template. Use the attached document as a guide for design, style, look and feel

Company name: Tarnwick Communities

I'll be happy to receive the document 80% complete so I can fill in the copy and minor details. All I need from a designer is to format and design a template that I can fill in

Thank you!

Target Market(s)

Corporate investors/clients

Font styles to use
Serif
Sans Serif

Requirements
Must have
• Please use the images of elderly people I have uploaded. There doesn't need to be a photo on every page, but please incorporate the images as you see fit. Also please use the logo attached 'Tarnwick Communities'
• Please see below the template layout/order page by page
• 1st page
• • Branding, photo of beach, headline saying capability statement
• 2nd page
• ABOUT US
• • High level overview from market/retail perspective of what Tarnwick offers and who we are
• • Talk about product and company philosophy
• 3rd page
• OUR TEAM
• • Photos, names and roles
• • Speak generally about immense team experience as a composite body of achievement
• 4th Page
• • List of projects and project values
• Page 5
• • More projects and project values
• Page 6
• • What we are offering our JV partners
• • Benefits and options of model
• Page 7
• • How Tarwick will change the market for the better/ difference between us and old models
• Final page
• • Branding, Address, company details. ABN/CAN
Should not have
• Please do NOT use bright/electric colours of blue, green or orange.
• Please use the attached document as a guide for style, colours and layout

```html
<!DOCTYPE html>
<html lang="en">
<head>
<meta charset="utf-8">
<title>Tarnwick Communities – Projects Spread</title>
<link rel="stylesheet" href="https://fonts.googleapis.com/css2?family=Arimo:wght@400&family=EB+Garamond:wght@400&display=swap">
<style>
  :root {
    --ink: #000000;
    --paper: #ffffff;
    --rule: #8a8a8a;
    --text: #111111;
    --sky-deep: #3f87cc;
    --sky-light: #9fcbee;
    --linen: #e9e6df;
    --sand: #cdb994;
    --pool-light: #d9ecfa;
    --pool: #2a8be0;
    --leaf-light: #a9bf73;
    --leaf: #5f7f2f;
    --leaf-dark: #3f5a20;
    --sea: #7fb3d8;
  }
  html, body { margin: 0; padding: 0; overflow: hidden; }
  body { background: var(--paper); }
  .canvas {
    position: relative; width: 1200px; height: 848px; overflow: hidden;
    background: var(--paper); font-family: "Arimo", Arial, sans-serif; color: var(--text);
  }
  .page-label {
    position: absolute; top: 16px; width: 200px; margin-left: -100px; text-align: center;
    font-family: "EB Garamond", Georgia, serif; font-size: 30px; font-weight: 400; color: var(--ink);
  }
  .page {
    position: absolute; top: 84px; height: 764px; width: 540px;
    border-top: 1px solid var(--rule); box-sizing: border-box;
  }
  .page--left { left: 66px; border-left: 1px solid var(--rule); border-right: 1px solid var(--rule); }
  .page--right { left: 606px; border-right: 1px solid var(--rule); }
  .sidebar { position: absolute; top: 0; width: 242px; height: 764px; }
  .page--left .sidebar { left: 0; }
  .page--right .sidebar { right: 0; }
  .brand {
    height: 53px; background: var(--ink); color: var(--paper);
    display: flex; align-items: center; justify-content: center;
    font-family: "Arimo", Arial, sans-serif; font-weight: 400; font-size: 14px;
  }
  .photo { width: 100%; }
  .photo--top { height: 221px; }
  .photo--bottom { height: 274px; }
  .photo--couple {
    background: linear-gradient(180deg, var(--sky-deep) 0%, var(--sky-light) 38%, var(--linen) 65%, var(--sand) 100%);
  }
  .photo--pool {
    background: linear-gradient(170deg, var(--pool-light) 0%, #8cc4ee 35%, #4aa3e8 65%, var(--pool) 100%);
  }
  .photo--cyclist {
    background: linear-gradient(180deg, var(--leaf-light) 0%, var(--leaf) 45%, #8f9a78 70%, var(--leaf-dark) 100%);
  }
  .photo--beach {
    background: linear-gradient(180deg, #8fbde6 0%, #c6dff2 30%, var(--sea) 52%, #e6dccb 70%, var(--sand) 100%);
  }
  .project-index {
    height: 216px; background: var(--ink); color: var(--paper);
    font-size: 11px; box-sizing: border-box; padding: 62px 0 0 30px;
  }
  .page--right .project-index { margin-left: -2px; padding-left: 33px; }
  .project-index__title { margin: 0 0 4px; font-weight: 400; font-size: 11px; line-height: 17px; }
  .project-index ul { list-style: none; margin: 0; padding: 0; }
  .project-index li { height: 17px; display: flex; align-items: center; }
  .project-index svg { width: 11px; height: 9px; margin-right: 5px; }
  .content { position: absolute; top: 0; width: 245px; height: 764px; }
  .page--left .content { left: 266px; }
  .page--right .content { left: 24px; }
  .section-banner {
    position: absolute; top: 90px; left: 0; width: 245px; height: 96px; margin: 0;
    background: var(--ink); color: var(--paper);
    font-size: 24px; font-weight: 400; letter-spacing: 0.5px;
    display: flex; align-items: center; justify-content: center;
  }
  .project { position: absolute; left: 2px; width: 250px; font-size: 11px; line-height: 13px; white-space: nowrap; }
  .project__tag {
    display: inline-block; background: var(--ink); color: var(--paper);
    font-size: 10.5px; line-height: 13px; padding: 0 1px; margin-bottom: 4px;
  }
  .project__tag--wide { width: 220px; }
  .project p { margin: 0 0 4px; }
</style>
</head>
<body>
<div class="canvas">
  <div class="page-label" style="left:328px">Page 4</div>
  <div class="page-label" style="left:840px">Page 5</div>

  <section class="page page--left">
    <aside class="sidebar">
      <header class="brand">Tarnwick Communities</header>
      <div class="photo photo--top photo--couple" role="img" aria-label="Photo of a smiling elderly couple sitting together on a beach"></div>
      <nav class="project-index">
        <h3 class="project-index__title">List of projects</h3>
        <ul>
          <li><svg viewBox="0 0 11 9"><path d="M0 4.5h9M5.5 1l3.5 3.5L5.5 8" stroke="#fff" stroke-width="1.5" fill="none"/></svg>Project 1</li>
          <li><svg viewBox="0 0 11 9"><path d="M0 4.5h9M5.5 1l3.5 3.5L5.5 8" stroke="#fff" stroke-width="1.5" fill="none"/></svg>Project 2</li>
          <li><svg viewBox="0 0 11 9"><path d="M0 4.5h9M5.5 1l3.5 3.5L5.5 8" stroke="#fff" stroke-width="1.5" fill="none"/></svg>Project 3</li>
          <li><svg viewBox="0 0 11 9"><path d="M0 4.5h9M5.5 1l3.5 3.5L5.5 8" stroke="#fff" stroke-width="1.5" fill="none"/></svg>Project 4</li>
        </ul>
      </nav>
      <div class="photo photo--bottom photo--pool" role="img" aria-label="Photo of an older swimmer with goggles and towel beside an indoor pool"></div>
    </aside>
    <div class="content">
      <h2 class="section-banner">PROJECTS</h2>
      <article class="project" style="top:215px">
        <span class="project__tag">Project1</span>
        <p>High level overview from market/retail perspective<br>of what Tarnwick offers and who we are</p>
        <p>Nulla lorem eros, hendrerit a mattis vel,<br>elementum aliquam nisi. Etiam vel sapien mi.<br>Cros nec varius ipsum. Interdum et malesuada<br>fames ac ante ipsum primis in faucibus.</p>
      </article>
      <article class="project" style="top:326px">
        <span class="project__tag">Project2</span>
        <p>High level overview from market/retail perspective<br>of what Tarnwick offers and who we are</p>
        <p>Nulla lorem eros, hendrerit a mattis vel,<br>elementum aliquam nisi. Etiam vel sapien mi.<br>Cros nec varius ipsum. Interdum et malesuada<br>fames ac ante ipsum primis in faucibus.</p>
      </article>
      <article class="project" style="top:437px">
        <span class="project__tag">Project3</span>
        <p>High level overview from market/retail perspective<br>of what Tarnwick offers and who we are</p>
        <p>Nulla lorem eros, hendrerit a mattis vel,<br>elementum aliquam nisi. Etiam vel sapien mi.<br>Cros nec varius ipsum. Interdum et malesuada<br>fames ac ante ipsum primis in faucibus.</p>
      </article>
      <article class="project" style="top:556px">
        <span class="project__tag">Project4</span>
        <p>High level overview from market/retail perspective<br>of what Tarnwick offers and who we are</p>
        <p>Nulla lorem eros, hendrerit a mattis vel,<br>elementum aliquam nisi. Etiam vel sapien mi.<br>Cros nec varius ipsum. Interdum et malesuada<br>fames ac ante ipsum primis in faucibus.</p>
      </article>
    </div>
  </section>

  <section class="page page--right">
    <div class="content">
      <h2 class="section-banner">PROJECTS</h2>
      <article class="project" style="top:215px">
        <span class="project__tag">Project5</span>
        <p>High level overview from market/retail perspective<br>of what Tarnwick offers and who we are</p>
        <p>Nulla lorem eros, hendrerit a mattis vel,<br>elementum aliquam nisi. Etiam vel sapien mi.<br>Cros nec varius ipsum. Interdum et malesuada<br>fames ac ante ipsum primis in faucibus.</p>
      </article>
      <article class="project" style="top:326px">
        <span class="project__tag project__tag--wide">Project6</span>
        <p style="margin-top:-4px">perspective of what Tarnwick offers and who we<br>are</p>
        <p style="margin-top:6px">Nulla lorem eros, hendrerit a mattis vel,<br>elementum aliquam nisi. Etiam vel sapien mi.<br>Cros nec varius ipsum. Interdum et malesuada<br>fames ac ante ipsum primis in faucibus.</p>
      </article>
      <article class="project" style="top:437px">
        <span class="project__tag">Project7</span>
        <p>High level overview from market/retail perspective<br>of what Tarnwick offers and who we are</p>
        <p>Nulla lorem eros, hendrerit a mattis vel,<br>elementum aliquam nisi. Etiam vel sapien mi.<br>Cros nec varius ipsum. Interdum et malesuada<br>fames ac ante ipsum primis in faucibus.</p>
      </article>
      <article class="project" style="top:556px">
        <span class="project__tag">Project8</span>
        <p>High level overview from market/retail perspective<br>of what Tarnwick offers and who we are</p>
        <p>Nulla lorem eros, hendrerit a mattis vel,<br>elementum aliquam nisi. Etiam vel sapien mi.<br>Cros nec varius ipsum. Interdum et malesuada<br>fames ac ante ipsum primis in faucibus.</p>
      </article>
    </div>
    <aside class="sidebar">
      <header class="brand">Tarnwick Communities</header>
      <div class="photo photo--top photo--cyclist" role="img" aria-label="Photo of a cheerful older man riding a bicycle among green trees"></div>
      <nav class="project-index">
        <h3 class="project-index__title">List of projects</h3>
        <ul>
          <li><svg viewBox="0 0 11 9"><path d="M0 4.5h9M5.5 1l3.5 3.5L5.5 8" stroke="#fff" stroke-width="1.5" fill="none"/></svg>Project 5</li>
          <li><svg viewBox="0 0 11 9"><path d="M0 4.5h9M5.5 1l3.5 3.5L5.5 8" stroke="#fff" stroke-width="1.5" fill="none"/></svg>Project 6</li>
          <li><svg viewBox="0 0 11 9"><path d="M0 4.5h9M5.5 1l3.5 3.5L5.5 8" stroke="#fff" stroke-width="1.5" fill="none"/></svg>Project 7</li>
          <li><svg viewBox="0 0 11 9"><path d="M0 4.5h9M5.5 1l3.5 3.5L5.5 8" stroke="#fff" stroke-width="1.5" fill="none"/></svg>Project 8</li>
        </ul>
      </nav>
      <div class="photo photo--bottom photo--beach" role="img" aria-label="Photo of a group of older friends in sun hats splashing along the shoreline"></div>
    </aside>
  </section>
</div>
</body>
</html>
```